FACE HARBOR

Labels for Men's Skin Care. Organic, target 25-35 The label will be 2x3.5 on a 4oz amber bottle. 3 labels with the information shown on the uploaded sample.
Our product is a e-commerce built to help my 24 year old twin sons have a business of their own. Although it will be sold online they will also do foot work and sell to barbers at barber shops using as a mist on customers after shaving. So we want something that will attract male customers and will look good in a modern Barbershop. This is there shot and packaging is very very important. So if you could help us out with a great label we would be working with you in the future for package design. Our line will have several mens Organic natural skin care cleanser, mask toners and moisturizers..Thank you for your help. We also hope to put our products in beauty supply shops. So it needs to stand out as a mans product but still be traditional male product. Oh be creative mind that you are and remember we are trying to build a brand that attracts 25-35 male. Thank you

Hello, I just wanted to let you know that I am up working very late.

for anyone on the other side of the world up and working. I sleep about
3 hours.. So I'll be up for a few more hours and then up again around 5am my time

Good morning... I just wanted to say I will need three labels.. The words on all three are not that different and will fit pretty much the same on all three. So if you could work with one showing how the colors might be a little different on the other two you can do that with just the one label Just to make it easier on you if you like.. we can fix the other two once I find the right label,  Thank you it is 3am here.. still working.. I love it.

Target Market(s)

MALE 25-35

Industry/Entity Type

E-Commerce

Requirements
Must have
• final design must be fitted to the dieline uploaded.

```html
<!DOCTYPE html>
<html lang="en">
<head>
<meta charset="utf-8">
<title>Face Harbor – Men's Skin Care Labels</title>
<link rel="stylesheet" href="https://fonts.googleapis.com/css2?family=PT+Sans:wght@400;700&family=Arimo:wght@400;700&display=swap">
<style>
  :root {
    --page-bg: #f4f1ec;
    --acai-light: #d3dc9c;
    --acai-mid: #a9b86a;
    --acai-deep: #7f9446;
    --acai-brand: #5a3a14;
    --acai-tag: #6f7f2e;
    --cran-light: #3f5224;
    --cran-deep: #1f2d14;
    --cran-band: #a6c52e;
    --cran-accent: #d8ea4e;
    --cream-light: #c9782a;
    --cream-deep: #9c4f12;
    --cream-head: #6b3510;
    --cream-gold: #f2c14a;
    --cream-text: #ffd86a;
    --band-dark: #2b2516;
    --ink-light: #ffffff;
    --ink-dark: #1f1a10;
  }
  * { box-sizing: border-box; margin: 0; padding: 0; }
  html, body { width: 1200px; height: 1020px; overflow: hidden; }
  body {
    background: var(--page-bg);
    font-family: "Arimo", Arial, sans-serif;
  }
  .label-row {
    display: flex;
    gap: 40px;
    justify-content: center;
    padding-top: 210px;
  }
  .label {
    position: relative;
    width: 340px;
    height: 600px;
    padding: 0;
    display: flex;
    flex-direction: column;
    overflow: hidden;
    box-shadow: 0 4px 16px rgba(0,0,0,.18);
  }
  .label__head {
    padding: 44px 0 28px;
    text-align: center;
  }
  .brand {
    font-family: "PT Sans", Arial, sans-serif;
    font-weight: 700;
    font-size: 46px;
    line-height: 1;
    letter-spacing: -0.5px;
  }
  .product-type {
    font-family: "PT Sans", Arial, sans-serif;
    font-size: 14px;
    letter-spacing: 2.4px;
    text-transform: uppercase;
    margin-top: 6px;
  }
  .flavor-band {
    margin: 30px 22px 0;
    padding: 11px 16px;
    font-family: "Arimo", Arial, sans-serif;
    font-weight: 700;
    font-size: 22px;
  }
  .tagline {
    padding: 16px 26px 0;
    font-weight: 700;
    font-size: 17px;
  }
  .claims {
    padding: 48px 26px 0;
    font-weight: 700;
    font-size: 14px;
    line-height: 1.45;
  }
  .claims p + p { margin-top: 22px; }
  .volume {
    position: absolute;
    left: 26px;
    bottom: 18px;
    font-size: 10px;
    font-weight: 700;
  }

  /* Acai Berry + Goat's Milk mist */
  .label--acai {
    background: linear-gradient(160deg, var(--acai-mid) 0%, var(--acai-deep) 100%);
    color: var(--ink-light);
  }
  .label--acai .label__head {
    background: linear-gradient(180deg, var(--acai-light), #bfcb82);
  }
  .label--acai .brand { color: var(--acai-brand); }
  .label--acai .product-type { color: var(--acai-tag); }
  .label--acai .flavor-band { background: var(--band-dark); color: var(--ink-light); }

  /* Cranberry + Pomegranate mist */
  .label--cran {
    background: linear-gradient(160deg, var(--cran-light) 0%, var(--cran-deep) 100%);
    color: var(--ink-light);
  }
  .label--cran .label__head {
    background: linear-gradient(180deg, #4b5f2a, var(--cran-light));
  }
  .label--cran .brand { color: var(--ink-light); }
  .label--cran .product-type { color: var(--cran-accent); }
  .label--cran .flavor-band { background: var(--cran-band); color: var(--ink-dark); }
  .label--cran .tagline { color: var(--cran-accent); }

  /* Soothing body cream */
  .label--cream {
    background: linear-gradient(170deg, var(--cream-light) 0%, var(--cream-deep) 100%);
    color: var(--cream-text);
  }
  .label--cream .label__head {
    background: linear-gradient(180deg, var(--cream-head), #7d4113);
  }
  .label--cream .brand { color: var(--ink-light); }
  .label--cream .product-type { color: var(--cream-gold); }
  .label--cream .flavor-band { background: var(--band-dark); color: var(--ink-light); }
  .label--cream .claims { padding-top: 40px; }
  .label--cream .volume { color: var(--ink-light); }
</style>
</head>
<body>
  <main class="label-row">
    <section class="label label--acai">
      <header class="label__head">
        <div class="brand">Face Harbor</div>
        <div class="product-type">Botanical Healing Mist</div>
      </header>
      <div class="flavor-band">Acai Berry+Goat's Milk</div>
      <div class="tagline">Daily Shave FIX For Men</div>
      <div class="claims">
        <p>Treats and Prevents Ingrown Hair and Calms Razor Bumps &amp; Burn After Shaving</p>
        <p>Refresh &amp; Moisturize</p>
      </div>
      <div class="volume">3.5 fl oz 103mL</div>
    </section>

    <section class="label label--cran">
      <header class="label__head">
        <div class="brand">Face Harbor</div>
        <div class="product-type">Botanical Healing Mist</div>
      </header>
      <div class="flavor-band">Cranberry+Pomegranate</div>
      <div class="tagline">Daily Shave FIX For Men</div>
      <div class="claims">
        <p>Facial Conditioner and Calms Razor Burns After Shaving</p>
        <p>Smooth Skin Blend</p>
      </div>
      <div class="volume">3.5 fl oz 103mL</div>
    </section>

    <section class="label label--cream">
      <header class="label__head">
        <div class="brand">Face Harbor</div>
        <div class="product-type">Soothing Body Cream</div>
      </header>
      <div class="flavor-band">Manhood Freshener</div>
      <div class="claims">
        <p>Organic Natural Healing</p>
        <p>Maintain Groin Freshness &amp; Dryness While Reducing Skin Irritation and Chafing</p>
      </div>
      <div class="volume">3.5 fl oz 103mL</div>
    </section>
  </main>
</body>
</html>
```